Jumbo direct mailing Postcard design

I need a design for an oversized postcard mailer that will be marketing a ballroom dance studio located in Cary, NC. We are an Vernon Callow franchised dance studio and considered the gold standard for ballroom dance lessons. Our instructors our certified and top quality. The size of the postcard is 8.5" x 5.5" and will be full color. Our website is carystepwell-example.com
This will be marketed to men and women. Average age is 30-60. Mostly females apply, but some males, see sliders.
We want an eye catching postcard to get people to call. We are offering a free dance lesson to people that either call or go to our website and fill out the form.
Some ideas we had for headlines are:
-
Bored in Cary? Looking for something new to try? Learn how to
-Spice up date night
-Meet new people at our dance parties
-Lose weight
-Gain confidence while learning a valuable social skill
-
We can discuss headlines and text in feedback discussion.
I will be uploading some creative assets you can use for this project, but are not required to be used at all. They are not the best looking creatives.
The final design should communicate a fun valuable social activity and skill to the reader and showing how our school is the best quality in the market. Using gold and black colors could accompany that.
Target Market(s)
men/women luxury market, age 30-60. affluent individuals
Industry/Entity Type
Dance Studio
Look and feel
Each slider illustrates characteristics of the customer's brand and the style your logo design should communicate.

```html
<!DOCTYPE html>
<html lang="en">
<head>
<meta charset="utf-8">
<title>Vernon Callow Dance Studios – Cary Postcard</title>
<link rel="stylesheet" href="https://fonts.googleapis.com/css2?family=Libre+Baskerville:wght@400;700&family=Tinos&display=swap">
<style>
  :root {
    --page-bg: #e4e4e4;
    --card-black: #070503;
    --card-brown: #2a1606;
    --gold: #c48c1c;
    --gold-bright: #e2a31c;
    --gold-deep: #8a5a0c;
    --text-light: #ffffff;
    --text-gold: #c28b1f;
  }
  html, body {
    margin: 0;
    width: 1200px;
    height: 900px;
    overflow: hidden;
    background: var(--page-bg);
  }
  .postcard {
    position: absolute;
    left: 40px;
    top: 88px;
    width: 1120px;
    height: 724px;
    overflow: hidden;
    background: var(--card-black);
    font-family: "Libre Baskerville", Georgia, serif;
  }
  .postcard__backdrop {
    position: absolute;
    inset: 0;
    width: 100%;
    height: 100%;
  }
  .postcard__glow {
    position: absolute;
    left: 0;
    top: 250px;
    width: 300px;
    height: 440px;
    background: radial-gradient(ellipse at 35% 45%, rgba(150, 95, 20, 0.45), rgba(90, 50, 10, 0.2) 45%, transparent 72%);
  }
  .brand {
    position: absolute;
    left: 624px;
    top: 68px;
    width: 470px;
    text-align: center;
    color: var(--text-light);
  }
  .brand__name {
    display: flex;
    align-items: center;
    justify-content: center;
    gap: 14px;
    font-family: "Libre Baskerville", Georgia, serif;
    font-weight: 700;
    font-size: 42px;
    line-height: 1;
  }
  .brand__dot {
    width: 12px;
    height: 12px;
    border-radius: 50%;
    background: var(--text-light);
  }
  .brand__tagline {
    margin-top: 8px;
    font-family: "Libre Baskerville", Georgia, serif;
    font-size: 14px;
    letter-spacing: 1px;
  }
  .headline {
    position: absolute;
    left: 47px;
    top: 296px;
    margin: 0;
    font-weight: 700;
    font-size: 52px;
    line-height: 58px;
  }
  .headline__lead { display: block; color: var(--text-light); }
  .headline__sub { display: block; color: var(--text-gold); }
  .benefits {
    position: absolute;
    left: 304px;
    top: 440px;
    font-family: "Tinos", "Times New Roman", serif;
  }
  .benefits__title {
    margin: 0 0 14px;
    font-size: 38px;
    font-weight: 400;
    color: var(--text-light);
    line-height: 1.1;
  }
  .benefits__list {
    list-style: none;
    margin: 0;
    padding: 0;
  }
  .benefits__item {
    position: relative;
    padding-left: 30px;
    font-size: 25px;
    line-height: 37.5px;
    color: var(--text-gold);
  }
  .benefits__item::before {
    content: "";
    position: absolute;
    left: 3px;
    top: 13px;
    width: 11px;
    height: 11px;
    border-radius: 50%;
    background: radial-gradient(circle at 35% 35%, #f6d37a, var(--gold-deep));
  }
</style>
</head>
<body>
  <main class="postcard">
    <svg class="postcard__backdrop" viewBox="0 0 978 632" preserveAspectRatio="none" aria-hidden="true">
      <defs>
        <linearGradient id="arcGold" x1="0" y1="0" x2="0" y2="1">
          <stop offset="0" stop-color="#2a1a06"/>
          <stop offset="0.55" stop-color="#8a5a0c"/>
          <stop offset="1" stop-color="#e2a31c"/>
        </linearGradient>
        <linearGradient id="swoopBrown" x1="0" y1="0" x2="1" y2="1">
          <stop offset="0" stop-color="#3a220a" stop-opacity="0.9"/>
          <stop offset="1" stop-color="#120904" stop-opacity="0.2"/>
        </linearGradient>
        <linearGradient id="edgeGold" x1="0" y1="0" x2="1" y2="0">
          <stop offset="0" stop-color="#c48c1c" stop-opacity="0"/>
          <stop offset="1" stop-color="#e2a31c" stop-opacity="0.8"/>
        </linearGradient>
      </defs>
      <rect width="978" height="632" fill="#070503"/>
      <path d="M0 0 H420 C300 60 140 140 0 230 Z" fill="url(#swoopBrown)" opacity="0.6"/>
      <path d="M0 300 C180 200 420 230 560 330 C420 280 200 300 0 400 Z" fill="#2a1606" opacity="0.5"/>
      <path d="M180 632 C420 520 720 470 978 520 V632 Z" fill="#1c0f05" opacity="0.8"/>
      <path d="M520 632 C700 560 860 520 978 560" fill="none" stroke="url(#edgeGold)" stroke-width="3"/>
      <path d="M760 632 C840 520 900 420 978 360" fill="none" stroke="#5a3a0c" stroke-width="2" opacity="0.7"/>
      <path d="M880 360 C920 300 950 250 978 230" fill="none" stroke="#4a6a1a" stroke-width="1.5" opacity="0.6"/>
      <ellipse cx="745" cy="40" rx="290" ry="168" fill="url(#arcGold)"/>
      <ellipse cx="745" cy="40" rx="298" ry="175" fill="none" stroke="#9a8a70" stroke-width="1" opacity="0.5"/>
      <path d="M0 250 C200 180 380 200 500 270" fill="none" stroke="#5a3a10" stroke-width="1" opacity="0.6"/>
      <path d="M0 520 C150 460 300 470 420 540" fill="none" stroke="#5a3a10" stroke-width="1" opacity="0.5"/>
    </svg>
    <div class="postcard__glow" role="img" aria-label="Soft golden bokeh light circles"></div>

    <div class="brand">
      <div class="brand__name"><span>Vernon Callow</span><span class="brand__dot"></span></div>
      <div class="brand__tagline">Franchised Dance Studios</div>
    </div>

    <h1 class="headline">
      <span class="headline__lead">Bored in Cary?</span>
      <span class="headline__sub">Looking for something new to try?</span>
    </h1>

    <section class="benefits">
      <h2 class="benefits__title">LEARN HOW TO</h2>
      <ul class="benefits__list">
        <li class="benefits__item">Spice up date night</li>
        <li class="benefits__item">Meet new people at our dance parties</li>
        <li class="benefits__item">Lose weight</li>
        <li class="benefits__item">Gain confidence while learning a valuable social skill</li>
      </ul>
    </section>
  </main>
</body>
</html>
```